CLEVER, EYE catching stationary for oil & gas technology company
Kelvor Subsurface Group
I need double sided standard sized Business Card [3.5" x 2"]
eurostile LT ExtendedTwo
Simple
Darren Holloway
Managing Partner
#22, 4307 - 3rd Avenue
Coldmere, MB
R4K 2M9
darren.holloway@kelvor.ca
www.kelvor.ca
Business cards will have rounded corners.
Back of business card we would like to see the Kelvor logo on a black back ground (but are open to other suggestions)
Centered on the back bottom part of card it should state: "Kelvor Subsurface Group Inc."

```html
<!DOCTYPE html>
<html lang="en">
<head>
<meta charset="utf-8">
<title>Kelvor Subsurface Group — Business Card</title>
<link href="https://fonts.googleapis.com/css2?family=Michroma&display=swap" rel="stylesheet">
<style>
  :root {
    --stage: #2b2b2d;
    --card-dark: #161616;
    --card-mid: #232323;
    --orange: #f06a1e;
    --orange-deep: #c9430f;
    --blue: #1f7fd6;
    --blue-deep: #0d4d9a;
    --text-grey: #b9b9b9;
    --text-dim: #8a8a8a;
  }
  html, body {
    margin: 0;
    width: 1200px;
    height: 864px;
    overflow: hidden;
    background: var(--stage);
    font-family: "Michroma", sans-serif;
  }
  .stage {
    position: relative;
    width: 1200px;
    height: 864px;
    display: flex;
    align-items: center;
    justify-content: center;
    gap: 40px;
  }
  .card {
    position: relative;
    width: 540px;
    height: 309px;
    border-radius: 18px;
    overflow: hidden;
    background: radial-gradient(ellipse at 40% 35%, var(--card-mid), var(--card-dark) 75%);
    box-shadow: 0 10px 30px rgba(0,0,0,.45);
  }

  /* Back */
  .back .brand-mark {
    position: absolute;
    left: 50%;
    top: 50%;
    transform: translate(-50%, -50%);
    display: flex;
    align-items: center;
    gap: 12px;
  }
  .brand-dot {
    width: 22px;
    height: 22px;
    border-radius: 50%;
    background: var(--orange);
  }
  .brand-name {
    color: var(--orange);
    font-size: 26px;
    letter-spacing: 2px;
    text-transform: uppercase;
  }
  .back .web-vertical {
    position: absolute;
    left: 30px;
    bottom: 26px;
    transform-origin: left bottom;
    transform: rotate(-90deg) translate(0, 100%);
    color: var(--orange);
    font-size: 11px;
    letter-spacing: 5px;
    text-transform: uppercase;
    white-space: nowrap;
  }

  /* Front */
  .front .logo-lockup {
    position: absolute;
    left: 56px;
    top: 70px;
    color: var(--orange);
    line-height: 1;
  }
  .logo-lockup .word {
    font-size: 40px;
    letter-spacing: 2px;
    text-transform: uppercase;
  }
  .logo-lockup .tag {
    margin-top: 8px;
    font-size: 13px;
    letter-spacing: .5px;
  }
  .person {
    position: absolute;
    left: 56px;
    top: 162px;
  }
  .person .name {
    color: var(--orange);
    font-size: 10px;
    letter-spacing: 1px;
    text-transform: uppercase;
  }
  .person .title {
    margin-top: 5px;
    color: var(--text-grey);
    font-size: 7.5px;
    letter-spacing: 1px;
    text-transform: uppercase;
  }
  .address {
    position: absolute;
    left: 56px;
    top: 212px;
    color: var(--text-grey);
    font-size: 8px;
    font-style: normal;
    line-height: 1.7;
    letter-spacing: .5px;
    text-transform: uppercase;
  }
  .contacts {
    position: absolute;
    left: 262px;
    top: 162px;
    list-style: none;
    margin: 0;
    padding: 0;
    color: var(--text-grey);
    font-size: 7.5px;
    letter-spacing: .5px;
  }
  .contacts li {
    display: flex;
    align-items: center;
    gap: 7px;
    margin-bottom: 7px;
  }
  .contacts .icon {
    width: 11px;
    height: 11px;
    border-radius: 50%;
    background: var(--orange);
    display: flex;
    align-items: center;
    justify-content: center;
  }
  .swoosh {
    position: absolute;
    right: 0;
    top: 0;
    width: 540px;
    height: 309px;
  }
</style>
</head>
<body>
<main class="stage">

  <section class="card back" aria-label="Card back">
    <div class="brand-mark">
      <span class="brand-dot"></span>
      <span class="brand-name">Kelvor</span>
    </div>
    <div class="web-vertical">www.kelvor.ca</div>
  </section>

  <section class="card front" aria-label="Card front">
    <svg class="swoosh" viewBox="0 0 540 309" aria-hidden="true">
      <defs>
        <linearGradient id="blueBand" x1="0" y1="0" x2="1" y2="1">
          <stop offset="0" stop-color="#1f7fd6"/>
          <stop offset="1" stop-color="#0d4d9a"/>
        </linearGradient>
        <linearGradient id="orangeBand" x1="0" y1="0" x2="1" y2="0">
          <stop offset="0" stop-color="#c9430f"/>
          <stop offset="1" stop-color="#f06a1e"/>
        </linearGradient>
      </defs>
      <path d="M540 60 C 505 120, 470 230, 380 309 L 540 309 Z" fill="url(#blueBand)"/>
      <path d="M540 48 C 498 120, 455 235, 356 309 L 372 309 C 462 236, 506 128, 540 70 Z" fill="url(#orangeBand)"/>
    </svg>

    <div class="logo-lockup">
      <div class="word">Kelvor</div>
      <div class="tag">Subsurface Group</div>
    </div>

    <div class="person">
      <div class="name">Darren Holloway</div>
      <div class="title">Managing Partner</div>
    </div>

    <address class="address">
      #22, 4307 - 3rd Avenue<br>
      Coldmere, MB R4K 2M9
    </address>

    <ul class="contacts">
      <li>
        <span class="icon">
          <svg width="7" height="7" viewBox="0 0 10 10"><path d="M2 1 L4 1 L4.6 3 L3.4 4 C4 5.4 4.8 6.2 6 6.6 L7 5.4 L9 6 L9 8 C5 8.5 1.5 5 2 1 Z" fill="#161616"/></svg>
        </span>
        555-214-0142
      </li>
      <li>
        <span class="icon">
          <svg width="7" height="7" viewBox="0 0 10 10"><rect x="1" y="2.5" width="8" height="5.5" fill="#161616"/><path d="M1 2.5 L5 6 L9 2.5" stroke="#f06a1e" fill="none" stroke-width="1"/></svg>
        </span>
        darren.holloway@kelvor.ca
      </li>
      <li>
        <span class="icon">
          <svg width="7" height="7" viewBox="0 0 10 10"><circle cx="5" cy="5" r="3.8" fill="none" stroke="#161616" stroke-width="1.2"/><path d="M1.2 5 H8.8 M5 1.2 V8.8" stroke="#161616" stroke-width="1"/></svg>
        </span>
        www.kelvor.ca
      </li>
    </ul>
  </section>

</main>
</body>
</html>
```